Powerpoint template for Marlow Brook Consulting

I need a powerpoint template for my business that would also work for Google slides.
I intermittently deliver training to people and I want a nice powerpoint template, that could also work in google docs to help make production easier and more seamless for me. I also sometimes product reports and analyses that are best done in powerpoint or Google slides. I need a title page, Title and content page, section heading page and any other pages that someone normally has!

Target Market(s)

Leaders and managers in medium to large companies. I provide training and coaching services to senior staff who have got 'stuck' and want help to find their way forward.

Font styles to use
Sans Serif

Requirements
Must have
• Colours and fonts to fit with logo please.
• Must include the logo and company name.
Nice to have
• a picture for the front?

```html
<!DOCTYPE html>
<html lang="en">
<head>
<meta charset="utf-8">
<title>Marlow Brook Consulting – Presentation Template</title>
<link rel="stylesheet" href="https://fonts.googleapis.com/css2?family=Montserrat:wght@400;600;700&family=Open+Sans:wght@400;600;700&family=Oswald:wght@400&display=swap">
<style>
  :root{
    --purple:#4b2d8f;
    --purple-soft:#6a4fb0;
    --teal:#1ea88e;
    --ink:#2b2b2b;
    --muted:#777;
    --rule:#cfcfcf;
    --stage-top:#ffffff;
    --stage-bottom:#9c9c9c;
    --white:#ffffff;
  }
  *{box-sizing:border-box;margin:0;padding:0}
  html,body{width:1200px;height:2632px;overflow:hidden}
  body{position:relative;background:var(--stage-bottom);font-family:"Open Sans",Arial,sans-serif;color:var(--ink)}
  .hero{position:absolute;left:0;top:0;width:1200px;height:807px;background:var(--stage-top)}
  .hero-frame{position:absolute;left:240px;top:190px;width:720px;height:405px;box-shadow:0 20px 40px rgba(0,0,0,.18)}
  .hero-frame .slide{position:absolute;left:0;top:0;transform:scale(1.3163);transform-origin:0 0;box-shadow:none}

  .slide{position:absolute;width:547px;height:307px;background:var(--white);overflow:hidden;box-shadow:0 10px 18px rgba(0,0,0,.28)}
  .col-l{left:35px}.col-r{left:617px}
  .row-1{top:863px}.row-2{top:1216px}.row-3{top:1568px}.row-4{top:1921px}.row-5{top:2273px}

  .abs{position:absolute}
  .brand{font-family:"Montserrat",Arial,sans-serif;font-weight:600;text-transform:uppercase;letter-spacing:.5px;line-height:1.15}
  .brand-dot{display:inline-block;border-radius:50%}

  /* header & footer */
  .slide-head{position:absolute;left:14px;right:46px;top:14px;height:18px;display:flex;align-items:center;gap:8px}
  .headline{flex:none;font-family:"Montserrat",Arial,sans-serif;font-weight:700;font-size:15px;line-height:18px;color:var(--ink);white-space:nowrap}
  .headline em{font-style:normal;color:var(--teal)}
  .head-rule{flex:1;height:1px;background:var(--purple)}
  .corner-mark{position:absolute;right:8px;top:8px;width:34px;font-size:5px;line-height:1.3;color:var(--teal);text-align:center}
  .corner-mark .brand-dot{width:14px;height:14px;background:var(--teal);margin-bottom:1px}
  .foot-rule{position:absolute;left:14px;right:14px;top:286px;height:1px;background:var(--rule)}
  .foot-url{position:absolute;left:0;right:0;top:290px;text-align:center;font-size:6px;letter-spacing:1.5px;color:var(--ink);font-weight:600}
  .foot-num{position:absolute;right:16px;top:290px;font-size:6px;color:var(--muted)}

  .tiny{font-size:5.5px;line-height:1.55;color:#555}
  .tiny-title{font-size:5.5px;font-weight:700;color:var(--purple);text-decoration:underline;text-transform:uppercase;margin-bottom:2px}
  .teal-title{font-size:6px;font-weight:700;color:var(--teal);text-transform:uppercase;margin-bottom:2px}

  /* covers */
  .cover-purple{background:var(--purple)}
  .cover-art{position:absolute;right:0;top:0;width:300px;height:307px;background:radial-gradient(ellipse at 60% 55%,rgba(255,255,255,.55),rgba(255,255,255,.08) 70%)}
  .cover-title{font-family:"Oswald","Montserrat",Arial,sans-serif;font-weight:400;color:var(--white);text-transform:uppercase;white-space:nowrap}
  .url-pill{position:absolute;left:0;top:272px;width:170px;height:16px;background:var(--white);border-radius:0 9px 9px 0;font-size:7px;font-weight:700;color:var(--purple);padding:3px 0 0 22px}

  .photo-fade{position:absolute;right:0;top:0;width:330px;height:307px;background:linear-gradient(90deg,rgba(255,255,255,1) 0%,rgba(196,207,190,.7) 35%,#aebea6 60%,#c9cfd2 100%)}
  .title-band{position:absolute;left:0;top:180px;width:510px;height:42px;background:var(--purple);clip-path:polygon(0 0,100% 0,94% 100%,0 100%);color:var(--white);font-family:"Montserrat",Arial,sans-serif;font-weight:600;font-size:18px;padding:10px 0 0 18px;text-transform:uppercase;white-space:nowrap}

  /* toc */
  .toc-row{position:absolute;left:72px;width:400px;height:12px;font-size:6px;color:#444;white-space:nowrap}
  .toc-row .lead{position:absolute;left:190px;width:180px;top:6px;border-top:1px dashed #aaa}
  .toc-row .num{position:absolute;right:0;top:0}
  .toc-row.sub{padding-left:10px}
  .toc-row.sub::before{content:"";position:absolute;left:0;top:2px;width:5px;height:5px;border-radius:50%;background:var(--teal)}

  .num-flag{position:absolute;width:16px;height:16px;background:var(--teal);clip-path:polygon(0 0,100% 0,0 100%);color:var(--white);font-size:5px;font-weight:700;padding:1px 0 0 3px}
  .icon-sq{position:absolute;width:16px;height:16px;background:var(--teal);border-radius:2px}
  .icon-sq::after{content:"";position:absolute;left:4px;top:4px;width:8px;height:8px;border:1px solid var(--white);border-radius:50%}

  .photo-box{position:absolute;left:0;top:44px;width:132px;height:96px;background:linear-gradient(180deg,#e8ebee,#c6ccd3 60%,#9aa2aa)}
  .quote-band{position:absolute;left:0;top:140px;width:180px;height:40px;background:var(--purple);clip-path:polygon(0 0,100% 0,92% 100%,0 100%);color:var(--white);font-size:5px;line-height:1.5;padding:6px 22px 0 8px}

  .box-card{position:absolute;width:168px;height:26px;border:1px solid var(--teal);font-size:5.5px;line-height:1.5;padding:4px 8px 0 14px;color:#444}
  .box-label{position:absolute;font-size:5px;font-weight:700;color:var(--purple);text-transform:uppercase}
  .people-dot{position:absolute;width:22px;height:22px;border-radius:50%;border:1px solid var(--teal);background:var(--white)}
  .people-dot::after{content:"";position:absolute;left:5px;top:5px;width:10px;height:10px;border-radius:50%;background:var(--purple)}
  .people-dot.plain{border:none;background:none}

  .step-title{font-size:5px;font-weight:700;color:var(--teal);text-transform:uppercase}
  .item-head{font-size:7px;font-weight:700;color:var(--purple)}

  .brand-large{position:absolute;left:760px;top:2320px;width:360px;text-align:center;color:var(--white)}
  .brand-large .brand-dot{width:70px;height:70px;background:var(--white);margin-bottom:18px}
  .brand-large .brand{font-size:30px;font-weight:400}
</style>
</head>
<body>

<section class="hero">
  <div class="hero-frame">
    <div class="slide cover-purple">
      <div class="cover-art" role="img" aria-label="Illustration of raised hands forming a tree with people figures"></div>
      <div class="abs brand" style="left:22px;top:60px;color:var(--white);font-size:13px;width:150px">Marlow Brook<br>Consulting</div>
      <div class="abs cover-title" style="left:22px;top:160px;font-size:19px">Presentation title goes here</div>
      <div class="abs" style="left:22px;top:186px;font-size:11px;color:var(--white)">Presentation subtitle goes here</div>
      <div class="url-pill">www.webaddress.com</div>
    </div>
  </div>
</section>

<!-- Cover with photo -->
<div class="slide col-l row-1">
  <div class="photo-fade" role="img" aria-label="Photo of a smiling businesswoman on the phone at a desk"></div>
  <div class="abs brand" style="left:18px;top:60px;color:var(--teal);font-size:12px;width:160px"><span class="brand-dot" style="width:10px;height:10px;background:var(--teal);margin-right:5px"></span>Marlow Brook<br>Consulting</div>
  <div class="title-band">Presentation title goes here</div>
</div>

<!-- Cover purple -->
<div class="slide cover-purple col-r row-1">
  <div class="cover-art" role="img" aria-label="Illustration of raised hands forming a tree with people figures"></div>
  <div class="abs brand" style="left:18px;top:70px;color:var(--white);font-size:12px;width:140px">Marlow Brook<br>Consulting</div>
  <div class="abs cover-title" style="left:18px;top:190px;font-size:16px">Presentation title goes here</div>
  <div class="abs" style="left:18px;top:212px;font-size:10px;color:var(--white)">Presentation subtitle goes here</div>
  <div class="url-pill" style="top:264px">www.webaddress.com</div>
</div>

<!-- Table of content -->
<div class="slide col-l row-2">
  <div class="slide-head"><div class="headline">TABLE OF <em>CONTENT</em></div><span class="head-rule"></span></div>
  <div class="corner-mark"><span class="brand-dot"></span><br>Marlow Brook</div>
  <div class="toc-row" style="top:72px">Lorem Ipsum is simply dummy text of the printing<span class="lead"></span><span class="num">03</span></div>
  <div class="toc-row sub" style="top:94px">Lorem Ipsum is simply dummy text<span class="lead"></span><span class="num">04</span></div>
  <div class="toc-row sub" style="top:116px">Lorem Ipsum is simply dummy text<span class="lead"></span><span class="num">05</span></div>
  <div class="toc-row" style="top:138px">Lorem Ipsum is simply dummy text of the printing<span class="lead"></span><span class="num">06</span></div>
  <div class="toc-row" style="top:160px">Lorem Ipsum is simply dummy text of the printing<span class="lead"></span><span class="num">07</span></div>
  <div class="toc-row" style="top:182px">Lorem Ipsum is simply dummy text of the printing<span class="lead"></span><span class="num">08</span></div>
  <div class="toc-row sub" style="top:204px">Lorem Ipsum is simply dummy text<span class="lead"></span><span class="num">09</span></div>
  <div class="toc-row" style="top:226px">Lorem Ipsum is simply dummy text of the printing<span class="lead"></span><span class="num">10</span></div>
  <div class="foot-rule"></div><div class="foot-url">www.webaddress.com</div><div class="foot-num">02</div>
</div>

<!-- Numbered grid -->
<div class="slide col-r row-2">
  <div class="slide-head"><div class="headline">HEADLINE <em>GOES HERE</em></div><span class="head-rule"></span></div>
  <div class="corner-mark"><span class="brand-dot"></span><br>Marlow Brook</div>
  <div class="num-flag" style="left:40px;top:90px">1</div>
  <div class="abs" style="left:60px;top:90px;width:80px"><div class="tiny-title">Your title here</div><div class="tiny">Lorem Ipsum is simply dummy text of the printing &amp; typesetting industry.</div></div>
  <div class="num-flag" style="left:212px;top:90px">2</div>
  <div class="abs" style="left:232px;top:90px;width:80px"><div class="tiny-title">Your title here</div><div class="tiny">Lorem Ipsum is simply dummy text of the printing &amp; typesetting industry.</div></div>
  <div class="num-flag" style="left:384px;top:90px">3</div>
  <div class="abs" style="left:404px;top:90px;width:80px"><div class="tiny-title">Your title here</div><div class="tiny">Lorem Ipsum is simply dummy text of the printing &amp; typesetting industry.</div></div>
  <div class="num-flag" style="left:40px;top:190px">4</div>
  <div class="abs" style="left:60px;top:190px;width:80px"><div class="tiny-title">Your title here</div><div class="tiny">Lorem Ipsum is simply dummy text of the printing &amp; typesetting industry.</div></div>
  <div class="num-flag" style="left:212px;top:190px">5</div>
  <div class="abs" style="left:232px;top:190px;width:80px"><div class="tiny-title">Your title here</div><div class="tiny">Lorem Ipsum is simply dummy text of the printing &amp; typesetting industry.</div></div>
  <div class="num-flag" style="left:384px;top:190px">6</div>
  <div class="abs" style="left:404px;top:190px;width:80px"><div class="tiny-title">Your title here</div><div class="tiny">Lorem Ipsum is simply dummy text of the printing &amp; typesetting industry.</div></div>
  <div class="foot-rule"></div><div class="foot-url">www.webaddress.com</div><div class="foot-num">03</div>
</div>

<!-- Photo + text -->
<div class="slide col-l row-3">
  <div class="slide-head"><div class="headline">HEADLINE <em>GOES HERE</em></div><span class="head-rule"></span></div>
  <div class="corner-mark"><span class="brand-dot"></span><br>Marlow Brook</div>
  <div class="photo-box" role="img" aria-label="Photo of a man working on a laptop"></div>
  <div class="quote-band">Lorem Ipsum is simply dummy text of the printing and typesetting industry. Lorem Ipsum has been the industry's standard dummy text ever since the 1500s.</div>
  <div class="abs" style="left:300px;top:78px;width:200px"><div class="teal-title">Your title here</div><div class="tiny">Lorem Ipsum is simply dummy text of the printing and typesetting industry. Lorem Ipsum has been the industry's standard dummy text ever since the 1500s.</div></div>
  <div class="abs" style="left:300px;top:140px;width:200px"><div class="teal-title">Your title here</div><div class="tiny">Lorem Ipsum is simply dummy text of the printing and typesetting industry. Lorem Ipsum has been the industry's standard dummy text ever since the 1500s.</div></div>
  <div class="abs" style="left:300px;top:202px;width:200px"><div class="teal-title">Your title here</div><div class="tiny">Lorem Ipsum is simply dummy text of the printing and typesetting industry. Lorem Ipsum has been the industry's standard dummy text ever since the 1500s.</div></div>
  <div class="foot-rule"></div><div class="foot-url">www.webaddress.com</div><div class="foot-num">04</div>
</div>

<!-- Icon grid -->
<div class="slide col-r row-3">
  <div class="slide-head"><div class="headline">HEADLINE <em>GOES HERE</em></div><span class="head-rule"></span></div>
  <div class="corner-mark"><span class="brand-dot"></span><br>Marlow Brook</div>
  <div class="icon-sq" style="left:40px;top:90px"></div>
  <div class="abs" style="left:62px;top:90px;width:80px"><div class="tiny-title">Your title here</div><div class="tiny">Lorem Ipsum is simply dummy text of the printing &amp; typesetting industry.</div></div>
  <div class="icon-sq" style="left:212px;top:90px"></div>
  <div class="abs" style="left:234px;top:90px;width:80px"><div class="tiny-title">Your title here</div><div class="tiny">Lorem Ipsum is simply dummy text of the printing &amp; typesetting industry.</div></div>
  <div class="icon-sq" style="left:384px;top:90px"></div>
  <div class="abs" style="left:406px;top:90px;width:80px"><div class="tiny-title">Your title here</div><div class="tiny">Lorem Ipsum is simply dummy text of the printing &amp; typesetting industry.</div></div>
  <div class="icon-sq" style="left:40px;top:190px"></div>
  <div class="abs" style="left:62px;top:190px;width:80px"><div class="tiny-title">Your title here</div><div class="tiny">Lorem Ipsum is simply dummy text of the printing &amp; typesetting industry.</div></div>
  <div class="icon-sq" style="left:212px;top:190px"></div>
  <div class="abs" style="left:234px;top:190px;width:80px"><div class="tiny-title">Your title here</div><div class="tiny">Lorem Ipsum is simply dummy text of the printing &amp; typesetting industry.</div></div>
  <div class="icon-sq" style="left:384px;top:190px"></div>
  <div class="abs" style="left:406px;top:190px;width:80px"><div class="tiny-title">Your title here</div><div class="tiny">Lorem Ipsum is simply dummy text of the printing &amp; typesetting industry.</div></div>
  <div class="foot-rule"></div><div class="foot-url">www.webaddress.com</div><div class="foot-num">05</div>
</div>

<!-- Cycle diagram -->
<div class="slide col-l row-4">
  <div class="slide-head"><div class="headline">HEADLINE <em>GOES HERE</em></div><span class="head-rule"></span></div>
  <div class="corner-mark"><span class="brand-dot"></span><br>Marlow Brook</div>
  <svg class="abs" style="left:30px;top:60px" width="190" height="190" viewBox="0 0 190 190" aria-hidden="true">
    <circle cx="95" cy="95" r="62" fill="none" stroke="var(--purple)" stroke-width="18"/>
    <circle cx="95" cy="33" r="20" fill="var(--teal)" stroke="#fff" stroke-width="3"/>
    <circle cx="95" cy="157" r="20" fill="var(--teal)" stroke="#fff" stroke-width="3"/>
    <circle cx="33" cy="95" r="20" fill="var(--teal)" stroke="#fff" stroke-width="3"/>
    <circle cx="157" cy="95" r="20" fill="var(--teal)" stroke="#fff" stroke-width="3"/>
    <circle cx="95" cy="95" r="14" fill="var(--teal)"/>
    <g fill="#fff"><circle cx="95" cy="29" r="4"/><circle cx="95" cy="153" r="4"/><circle cx="29" cy="95" r="4"/><circle cx="161" cy="95" r="4"/></g>
  </svg>
  <div class="abs" style="left:275px;top:72px;font-family:'Montserrat',Arial,sans-serif;font-weight:700;font-size:10px">Title <span style="color:var(--teal)">Goes Here</span></div>
  <div class="abs" style="left:275px;top:96px;width:200px"><div class="step-title">Step - 1</div><div class="tiny">Lorem Ipsum is simply dummy text of the printing and typesetting industry. Lorem Ipsum has been the industry's standard.</div></div>
  <div class="abs" style="left:275px;top:134px;width:200px"><div class="step-title">Step - 2</div><div class="tiny">Lorem Ipsum is simply dummy text of the printing and typesetting industry. Lorem Ipsum has been the industry's standard.</div></div>
  <div class="abs" style="left:275px;top:172px;width:200px"><div class="step-title">Step - 3</div><div class="tiny">Lorem Ipsum is simply dummy text of the printing and typesetting industry. Lorem Ipsum has been the industry's standard.</div></div>
  <div class="abs" style="left:275px;top:210px;width:200px"><div class="step-title">Step - 4</div><div class="tiny">Lorem Ipsum is simply dummy text of the printing and typesetting industry. Lorem Ipsum has been the industry's standard.</div></div>
  <div class="foot-rule"></div><div class="foot-url">www.webaddress.com</div><div class="foot-num">06</div>
</div>

<!-- Boxed headings -->
<div class="slide col-r row-4">
  <div class="slide-head"><div class="headline">HEADLINE <em>GOES HERE</em></div><span class="head-rule"></span></div>
  <div class="corner-mark"><span class="brand-dot"></span><br>Marlow Brook</div>
  <div class="box-label" style="left:48px;top:76px">Heading here</div>
  <div class="box-card" style="left:36px;top:86px">Lorem Ipsum is simply dummy text of the printing and typesetting industry.</div>
  <div class="people-dot" style="left:24px;top:80px"></div>
  <div class="box-label" style="left:332px;top:76px">Heading here</div>
  <div class="box-card" style="left:320px;top:86px">Lorem Ipsum is simply dummy text of the printing and typesetting industry.</div>
  <div class="people-dot" style="left:308px;top:80px"></div>
  <div class="box-label" style="left:48px;top:168px">Heading here</div>
  <div class="box-card" style="left:36px;top:178px">Lorem Ipsum is simply dummy text of the printing and typesetting industry.</div>
  <div class="people-dot" style="left:24px;top:172px"></div>
  <div class="box-label" style="left:332px;top:168px">Heading here</div>
  <div class="box-card" style="left:320px;top:178px">Lorem Ipsum is simply dummy text of the printing and typesetting industry.</div>
  <div class="people-dot" style="left:308px;top:172px"></div>
  <div class="foot-rule"></div><div class="foot-url">www.webaddress.com</div><div class="foot-num">07</div>
</div>

<!-- Chart -->
<div class="slide col-l row-5">
  <div class="slide-head"><div class="headline">HEADLINE <em>GOES HERE</em></div><span class="head-rule"></span></div>
  <div class="corner-mark"><span class="brand-dot"></span><br>Marlow Brook</div>
  <svg class="abs" style="left:20px;top:80px" width="250" height="140" viewBox="0 0 250 140" aria-label="Line chart with two series" role="img">
    <g stroke="#e2e2e2" stroke-width="1"><line x1="20" y1="10" x2="245" y2="10"/><line x1="20" y1="50" x2="245" y2="50"/><line x1="20" y1="90" x2="245" y2="90"/></g>
    <g font-size="5" fill="#888" font-family="Open Sans, sans-serif"><text x="2" y="12">100</text><text x="2" y="52">50</text><text x="2" y="92">0</text></g>
    <polyline fill="none" stroke="var(--teal)" stroke-width="1.5" points="25,70 65,40 105,58 145,55 185,45 225,16"/>
    <polyline fill="none" stroke="var(--purple)" stroke-width="1.5" points="25,80 65,68 105,84 145,70 185,78 225,50"/>
    <g fill="#fff" stroke-width="1.5"><circle cx="65" cy="40" r="3" stroke="var(--teal)"/><circle cx="145" cy="55" r="3" stroke="var(--teal)"/><circle cx="225" cy="16" r="3" stroke="var(--teal)"/><circle cx="65" cy="68" r="3" stroke="var(--purple)"/><circle cx="145" cy="70" r="3" stroke="var(--purple)"/><circle cx="225" cy="50" r="3" stroke="var(--purple)"/></g>
    <text x="25" y="112" font-size="5.5" fill="#555" font-family="Open Sans, sans-serif">Lorem Ipsum is simply dummy text of the printing and typesetting.</text>
    <circle cx="30" cy="128" r="3" fill="none" stroke="var(--teal)"/><text x="37" y="130" font-size="5" fill="#555" font-family="Open Sans, sans-serif">Title Here</text>
    <circle cx="100" cy="128" r="3" fill="none" stroke="#888"/><text x="107" y="130" font-size="5" fill="#555" font-family="Open Sans, sans-serif">Title Here</text>
  </svg>
  <div class="people-dot plain" style="left:300px;top:98px"></div>
  <div class="abs" style="left:330px;top:98px;width:170px"><div class="item-head">Heading Here</div><div class="tiny">Lorem Ipsum is simply dummy text of the printing and typesetting industry.</div></div>
  <div class="people-dot plain" style="left:300px;top:148px"></div>
  <div class="abs" style="left:330px;top:148px;width:170px"><div class="item-head">Heading Here</div><div class="tiny">Lorem Ipsum is simply dummy text of the printing and typesetting industry.</div></div>
  <div class="people-dot plain" style="left:300px;top:198px"></div>
  <div class="abs" style="left:330px;top:198px;width:170px"><div class="item-head">Heading Here</div><div class="tiny">Lorem Ipsum is simply dummy text of the printing and typesetting industry.</div></div>
  <div class="foot-rule"></div><div class="foot-url">www.webaddress.com</div><div class="foot-num">08</div>
</div>

<div class="brand-large">
  <span class="brand-dot"></span>
  <div class="brand">Marlow Brook<br>Consulting</div>
</div>

</body>
</html>
```